Regenerative Medicine - Medical - Patient Informational Flyer

I am looking to create an informational flyer for our patients. We use a regenerative medicine product for injections. It would be similar to a PRP flyer, but using the information below.
Front of Flyer
Headline:
"Unlock the Healing Power of Umbilical Cord Tissue Allograft"
Subheadline:
"Supporting Your Body's Natural Healing with Advanced Tissue Therapy"
Introduction:
A brief, engaging introduction that explains what umbilical cord tissue allograft is and why it’s an innovative option for patients seeking to enhance their body's healing process.
Inside of Flyer
Section 1: What is Umbilical Cord Tissue Allograft?
Description: Explain that umbilical cord tissue allograft is a regenerative treatment derived from the umbilical cord, specifically designed to support the body’s natural healing mechanisms.
Source: Emphasize that the tissue is ethically sourced from healthy, full-term births.
Section 2: Structural Tissue Components & Their Benefits
Overview: Explain that the umbilical cord tissue contains essential structural components such as collagen, growth factors, and extracellular matrix.
Key Points:
Collagen:
Benefit: Provides a natural scaffold that supports tissue repair and regeneration.
How it Helps: Enhances structural integrity and strength to damaged tissues.
Growth Factors:
Benefit: Promote cellular growth and healing.
How it Helps: Stimulates tissue repair, reduces inflammation, and accelerates the healing process.
Extracellular Matrix (ECM):
Benefit: Provides a framework for cells to adhere to, facilitating the reconstruction of damaged tissues.
How it Helps: Enhances tissue repair by mimicking the body's natural healing environment.
Section 3: Applications and Uses
Orthopedic Care: Highlight how the allograft can be used in joint and soft tissue injuries, particularly in enhancing the healing of ligaments, tendons, and cartilage.
Wound Healing: Discuss its use in difficult-to-heal wounds, providing a foundation for tissue regrowth and faster recovery.
Cosmetic and Reconstructive Surgery: Mention its benefits in skin repair and aesthetic procedures.
Back of Flyer
Section 4: What to Expect from the Treatment
Procedure: Briefly explain how the allograft is administered, typically through injection or surgical application.
Safety and Efficacy: Reassure patients that the procedure is safe, with minimal risk, and has been shown to effectively support healing and tissue regeneration.
Section 5: Why Choose Our Clinic?
Expert Care: Emphasize the expertise of your medical team in administering this advanced treatment.
Patient Testimonials: Include a brief testimonial or quote from a satisfied patient (if available).
Contact Information: Provide your clinic's contact details and encourage patients to schedule a consultation.
Design Tips:
Use soothing, natural colors like blues and greens to convey trust and health.
Include high-quality images of happy, active individuals to reinforce the benefits of the treatment.
Ensure that the text is easy to read, with headings and bullet points to break down information clearly.

```html
<!DOCTYPE html>
<html lang="en">
<head>
<meta charset="utf-8">
<title>Crestline Health &amp; Wellness – Umbilical Cord Tissue Allograft Trifold</title>
<link href="https://fonts.googleapis.com/css2?family=Roboto:wght@400;500;700&family=Oswald:wght@500;600&display=swap" rel="stylesheet">
<style>
:root{
  --backdrop:#7d8286;
  --navy:#1e3c6c;
  --navy-deep:#172f57;
  --blue:#2b6cb4;
  --blue-mid:#3e80c1;
  --blue-box:#3a7ab8;
  --sky:#a9c9e7;
  --paper:#ffffff;
  --ink:#26282c;
  --soft-ink:#e7eef8;
}
*{box-sizing:border-box;margin:0;padding:0}
html,body{width:1200px;height:2734px;overflow:hidden}
body{background:var(--backdrop);font-family:"Roboto",Arial,sans-serif;color:var(--ink);position:relative}
.spread{position:absolute;left:60px;width:1080px;height:832px;display:flex;box-shadow:0 8px 30px rgba(0,0,0,.25)}
.spread--outside{top:495px}
.spread--inside{top:1407px}
.panel{position:relative;width:360px;height:832px;overflow:hidden}
.panel--white{background:var(--paper)}
.panel--navy{background:var(--navy);color:#fff}
.panel--white::after{content:"";position:absolute;top:0;bottom:0;right:0;width:18px;background:linear-gradient(90deg,rgba(0,0,0,0),rgba(0,0,0,.06))}
.photo{position:absolute;left:0;width:100%}
.wave{position:absolute;left:0;width:100%}

/* numbered benefit lists */
.benefits{position:absolute;left:30px;right:30px}
.benefit{position:relative;padding-left:27px;margin-bottom:14px}
.benefit::before{content:"";position:absolute;left:9px;top:22px;bottom:-14px;border-left:2px dotted var(--navy)}
.benefit:last-child::before{bottom:0}
.benefit__num{position:absolute;left:0;top:0;width:20px;height:20px;border-radius:50%;background:var(--navy);color:#fff;font:700 12px/20px "Roboto",sans-serif;text-align:center}
.benefit__title{font:700 15.5px/1.2 "Roboto",sans-serif;color:var(--blue);margin-bottom:4px}
.body{font-size:10.6px;line-height:1.32;text-align:justify;margin-bottom:7px}
.body b{font-weight:700;color:var(--navy)}
.panel--navy .body b{color:#fff}

/* intro panel */
.intro{position:absolute;top:34px;left:34px;right:34px;text-align:center}
.intro__title{font:700 16px/1.2 "Roboto",sans-serif;margin-bottom:4px}
.intro__text{font-size:13px;line-height:1.32}
.brand{display:flex;align-items:center;gap:8px;font:700 20px/1 "Roboto",sans-serif;letter-spacing:.3px}
.brand__dot{width:16px;height:16px;border-radius:50%;flex:none}
.contact{position:absolute;top:475px;left:20px;right:20px;text-align:center}
.contact .brand{justify-content:center;color:#fff;margin-bottom:26px}
.contact .brand__dot{background:#fff}
.contact__title{font:700 15px/1 "Roboto",sans-serif;text-decoration:underline;text-underline-offset:3px;margin-bottom:14px}
.contact__item{font-size:13px;line-height:1.3;margin-bottom:10px}
.contact__icon{display:block;margin:0 auto 5px;width:16px;height:16px}

/* cover */
.cover .brand{position:absolute;top:38px;left:0;right:0;justify-content:center;color:var(--navy)}
.cover .brand__dot{background:var(--navy)}
.cover__text{position:absolute;top:585px;left:20px;right:20px;text-align:center}
.cover__headline{font:600 23px/1.2 "Oswald",sans-serif;color:var(--navy);text-transform:uppercase;letter-spacing:.2px}
.cover__sub{font:500 15px/1.3 "Roboto",sans-serif;color:var(--navy-deep);margin-top:14px}
.url-pill{display:inline-block;margin-top:14px;background:var(--navy);color:#fff;border-radius:16px;padding:6px 24px;font:500 14px/1.2 "Roboto",sans-serif}

/* inside sections */
.section{position:absolute;left:32px;right:30px}
.section__label{font:700 15px/1.2 "Roboto",sans-serif;color:var(--blue);text-decoration:underline;text-underline-offset:3px}
.section__sub{font:700 12px/1.3 "Roboto",sans-serif;color:var(--navy);margin:3px 0 6px}
.panel--navy .section__label{color:#fff}
.panel--navy .section__sub{color:#fff;font-weight:500}
.icon-row{display:flex;gap:10px;margin-bottom:9px}
.icon-ring{flex:none;width:38px;height:38px;border-radius:50%;border:1.5px solid rgba(255,255,255,.85);background:var(--blue-mid);display:flex;align-items:center;justify-content:center}
.icon-ring svg{width:20px;height:20px}
.icon-row .body{margin:0}

.key-box{position:absolute;left:32px;right:30px;top:300px;height:425px;border-radius:10px;background:linear-gradient(180deg,#4f90cc,#3676b4);color:#fff;padding:44px 14px 10px 12px}
.key-box__tag{position:absolute;top:10px;left:0;background:var(--navy);padding:6px 12px;font:700 14px/1 "Roboto",sans-serif;border-radius:0 10px 10px 0}
.key{display:flex;gap:10px;margin-bottom:10px}
.key .icon-ring{width:42px;height:42px;background:rgba(255,255,255,.12);margin-top:6px}
.key__title{font:700 12.5px/1.2 "Roboto",sans-serif;margin-bottom:2px}
.key .body{font-size:10px;margin-bottom:5px;color:var(--soft-ink)}
.key .body b{color:#fff}

.why-box{position:absolute;left:32px;right:30px;top:482px;height:245px;border-radius:10px;background:var(--blue-box);padding:14px 12px 10px}
.why-box .section__label,.why-box .section__sub{color:#fff}
.why-box .icon-ring{background:rgba(255,255,255,.1)}
.why-box .body{font-size:10px}

.lead{position:absolute;top:22px;left:30px;right:30px;font:700 11px/1.32 "Roboto",sans-serif;color:var(--ink);text-align:justify}
</style>
</head>
<body>

<!-- OUTSIDE SPREAD -->
<section class="spread spread--outside">

  <div class="panel panel--white">
    <div class="benefits" style="top:34px">
      <div class="benefit">
        <span class="benefit__num">5</span>
        <h3 class="benefit__title">Extracellular Matrix (ECM) Components</h3>
        <p class="body"><b>Benefit:</b> The ECM provides a natural scaffold that supports the regeneration of tissues. It mimics the body's natural environment, which helps cells to attach, grow, and organize into new tissue.</p>
        <p class="body"><b>Application:</b> Beneficial for all types of injuries, especially those involving complex tissue structures like tendons and soft tissues.</p>
      </div>
      <div class="benefit">
        <span class="benefit__num">6</span>
        <h3 class="benefit__title">Immunomodulatory Effects</h3>
        <p class="body"><b>Benefit:</b> Umbilical cord tissue has properties that can modulate the immune system, reducing the risk of excessive immune reactions and potential tissue rejection.</p>
        <p class="body"><b>Application:</b> Important in tendon and soft tissue injuries, where immune responses can sometimes hinder the healing process.</p>
      </div>
      <div class="benefit">
        <span class="benefit__num">7</span>
        <h3 class="benefit__title">Minimally Invasive Treatment Option</h3>
        <p class="body"><b>Benefit:</b> Utilizing umbilical cord tissue for treating injuries is minimally invasive, reducing the risk of complications and leading to quicker recovery times compared to more invasive surgical options.</p>
        <p class="body"><b>Application:</b> Suitable for patients seeking less invasive treatment options for joint, tendon, and soft tissue injuries.</p>
      </div>
    </div>
    <div class="photo" style="top:572px;height:260px;background:linear-gradient(135deg,#cfe3f3 0%,#6fb2de 35%,#e9c5b2 60%,#3f8fc2 100%)" role="img" aria-label="Gloved clinician giving an injection into a patient's shoulder"></div>
    <svg class="wave" style="top:566px" width="360" height="50" viewBox="0 0 360 50" aria-hidden="true">
      <path d="M0 0H360V8Q190 50 0 22Z" fill="#fff"/>
      <path d="M0 22Q190 50 360 8" fill="none" stroke="#1e3c6c" stroke-width="3"/>
    </svg>
  </div>

  <div class="panel panel--navy">
    <div class="intro">
      <h2 class="intro__title">INTRODUCTION:</h2>
      <p class="intro__text">A brief, engaging introduction that explains what umbilical cord tissue allograft is and why it's an innovative option for patients seeking to enhance their body's healing process.</p>
    </div>
    <div class="photo" style="top:205px;height:235px;background:radial-gradient(ellipse at 50% 45%,#3a5d8f 0%,#28497a 45%,#1e3c6c 80%)" role="img" aria-label="Patient and clinician reviewing information together at a desk"></div>
    <div class="contact">
      <div class="brand"><span class="brand__dot"></span>Crestline Health &amp; Wellness</div>
      <p class="contact__title">CONTACT US</p>
      <div class="contact__item">
        <svg class="contact__icon" viewBox="0 0 16 16" aria-hidden="true"><circle cx="8" cy="8" r="8" fill="#fff"/><path d="M8 3.5a2.8 2.8 0 0 0-2.8 2.8c0 2 2.8 5.2 2.8 5.2s2.8-3.2 2.8-5.2A2.8 2.8 0 0 0 8 3.5zm0 3.9a1.1 1.1 0 1 1 0-2.2 1.1 1.1 0 0 1 0 2.2z" fill="#1e3c6c"/></svg>
        482 Linden Park Road, Fairview,<br>Ohio 43000
      </div>
      <div class="contact__item">
        <svg class="contact__icon" viewBox="0 0 16 16" aria-hidden="true"><circle cx="8" cy="8" r="8" fill="#fff"/><path d="M5.4 4.2l1.3 1.6-.7 1.1a5 5 0 0 0 2.2 2.2l1.1-.7 1.6 1.3-.6 1.3c-3 .2-6.2-3-6-6z" fill="#1e3c6c"/></svg>
        555-014-2290
      </div>
      <div class="contact__item">
        <svg class="contact__icon" viewBox="0 0 16 16" aria-hidden="true"><circle cx="8" cy="8" r="8" fill="#fff"/><rect x="4" y="5.2" width="8" height="5.6" rx=".6" fill="#1e3c6c"/><path d="M4.3 5.6L8 8.4l3.7-2.8" stroke="#fff" stroke-width=".8" fill="none"/></svg>
        info@crestlinehw.com
      </div>
      <div class="contact__item">
        <svg class="contact__icon" viewBox="0 0 16 16" aria-hidden="true"><circle cx="8" cy="8" r="8" fill="#fff"/><g fill="none" stroke="#1e3c6c" stroke-width=".9"><circle cx="8" cy="8" r="4.2"/><ellipse cx="8" cy="8" rx="1.8" ry="4.2"/><path d="M3.8 8h8.4"/></g></svg>
        www.crestlinehealthoh.com
      </div>
    </div>
  </div>

  <div class="panel panel--white cover">
    <div class="brand"><span class="brand__dot"></span>Crestline Health &amp; Wellness</div>
    <div class="photo" style="top:100px;height:470px;background:linear-gradient(160deg,#f1f3f5 0%,#dfe4e8 30%,#58a6db 55%,#d9b39c 75%,#c89a82 100%)" role="img" aria-label="Doctor in white coat injecting a patient's knee with gloved hands"></div>
    <svg class="wave" style="top:88px" width="360" height="40" viewBox="0 0 360 40" aria-hidden="true">
      <path d="M0 0H360V28Q180 -4 0 22Z" fill="#fff"/>
      <path d="M0 22Q180 -4 360 28" fill="none" stroke="#1e3c6c" stroke-width="3"/>
    </svg>
    <svg class="wave" style="top:538px" width="360" height="294" viewBox="0 0 360 294" aria-hidden="true">
      <path d="M0 26Q180 -6 360 26V294H0Z" fill="#a9c9e7"/>
      <path d="M0 26Q180 -6 360 26" fill="none" stroke="#1e3c6c" stroke-width="4"/>
    </svg>
    <div class="cover__text">
      <h1 class="cover__headline">Unlock the Healing<br>Power of Umbilical Cord<br>Tissue Allograft</h1>
      <p class="cover__sub">Supporting Your Body's<br>Natural Healing with Advanced<br>Tissue Therapy</p>
      <span class="url-pill">www.crestlinehealthoh.com</span>
    </div>
  </div>
</section>

<!-- INSIDE SPREAD -->
<section class="spread spread--inside">

  <div class="panel panel--white">
    <div class="section" style="top:28px">
      <h2 class="section__label">SECTION 1:</h2>
      <p class="section__sub">What is Umbilical Cord Tissue Allograft?</p>
      <p class="body"><b>Description:</b> Explain that umbilical cord tissue allograft is a regenerative treatment derived from the umbilical cord, specifically designed to support the body's natural healing mechanisms.</p>
      <p class="body"><b>Source:</b> Emphasize that the tissue is ethically sourced from healthy, full-term births.</p>
    </div>
    <div class="section" style="top:204px">
      <h2 class="section__label">SECTION 2:</h2>
      <p class="body" style="margin-top:8px"><b>Structural Tissue Components and Their Benefits Overview:</b> Explain that the umbilical cord tissue contains essential structural components such as collagen, growth factors, and extracellular matrix.</p>
    </div>
    <div class="key-box">
      <span class="key-box__tag">KEY POINTS:</span>
      <div class="key">
        <span class="icon-ring"><svg viewBox="0 0 20 20" aria-hidden="true"><g fill="none" stroke="#fff" stroke-width="1.4"><circle cx="7" cy="8" r="3.5"/><circle cx="13" cy="8" r="3.5"/><circle cx="10" cy="13" r="3.5"/></g></svg></span>
        <div>
          <p class="key__title">Collagen:</p>
          <p class="body"><b>Benefit:</b> Provides a natural scaffold that supports tissue repair and regeneration.</p>
          <p class="body"><b>How it Helps:</b> Enhances structural integrity and strength to damaged tissues.</p>
        </div>
      </div>
      <div class="key">
        <span class="icon-ring"><svg viewBox="0 0 20 20" aria-hidden="true"><g fill="#fff"><rect x="3" y="12" width="3" height="5"/><rect x="8" y="9" width="3" height="8"/><rect x="13" y="6" width="3" height="11"/></g><path d="M3 9l5-4 3 2 6-5" fill="none" stroke="#fff" stroke-width="1.3"/></svg></span>
        <div>
          <p class="key__title">Growth Factors:</p>
          <p class="body"><b>Benefit:</b> Promote cellular growth and healing.</p>
          <p class="body"><b>How it Helps:</b> Stimulates tissue repair, reduces inflammation, and accelerates the healing process.</p>
        </div>
      </div>
      <div class="key">
        <span class="icon-ring"><svg viewBox="0 0 20 20" aria-hidden="true"><g fill="none" stroke="#fff" stroke-width="1.3"><rect x="3" y="3" width="14" height="14" rx="1"/><path d="M3 8h14M3 12h14M8 3v14M12 3v14"/></g></svg></span>
        <div>
          <p class="key__title">Extracellular Matrix (ECM):</p>
          <p class="body"><b>Benefit:</b> Provides a framework for cells to adhere to, facilitating the reconstruction of damaged tissues.</p>
          <p class="body"><b>How it Helps:</b> Enhances tissue repair by mimicking the body's natural healing environment.</p>
        </div>
      </div>
    </div>
  </div>

  <div class="panel panel--navy">
    <div class="section" style="top:28px">
      <h2 class="section__label">SECTION 3:</h2>
      <p class="section__sub">Applications and Uses</p>
      <div class="icon-row">
        <span class="icon-ring"><svg viewBox="0 0 20 20" aria-hidden="true"><path d="M7 2v6l-2 3v7M13 2v6l2 3v7" fill="none" stroke="#fff" stroke-width="1.5"/><circle cx="10" cy="10" r="2" fill="#fff"/></svg></span>
        <p class="body"><b>Orthopedic Care:</b> Highlight how the allograft can be used in joint and soft tissue injuries, particularly in enhancing the healing of ligaments, tendons, and cartilage.</p>
      </div>
      <div class="icon-row">
        <span class="icon-ring"><svg viewBox="0 0 20 20" aria-hidden="true"><g fill="none" stroke="#fff" stroke-width="1.5"><rect x="2" y="7" width="16" height="6" rx="3" transform="rotate(45 10 10)"/><rect x="2" y="7" width="16" height="6" rx="3" transform="rotate(-45 10 10)"/></g></svg></span>
        <p class="body"><b>Wound Healing:</b> Discuss its use in difficult-to-heal wounds, providing a foundation for tissue regrowth and faster recovery.</p>
      </div>
      <div class="icon-row">
        <span class="icon-ring"><svg viewBox="0 0 20 20" aria-hidden="true"><g fill="none" stroke="#fff" stroke-width="1.5"><path d="M4 17c0-4 3-6 6-6s6 2 6 6"/><path d="M6 6l8 0M6 9l8 0"/></g></svg></span>
        <p class="body"><b>Cosmetic &amp; Reconstructive Surgery:</b> Mention its benefits in skin repair and aesthetic procedures.</p>
      </div>
    </div>
    <div class="section" style="top:290px">
      <h2 class="section__label">SECTION 4:</h2>
      <p class="section__sub">What to Expect from the Treatment</p>
      <div class="icon-row">
        <span class="icon-ring"><svg viewBox="0 0 20 20" aria-hidden="true"><g fill="none" stroke="#fff" stroke-width="1.4"><rect x="5" y="3" width="10" height="14" rx="1"/><path d="M8 7h4M8 10h4M8 13h3"/></g></svg></span>
        <p class="body"><b>Procedure:</b> Briefly explain how the allograft is administered, typically through injection or surgical application.</p>
      </div>
      <div class="icon-row">
        <span class="icon-ring"><svg viewBox="0 0 20 20" aria-hidden="true"><path d="M10 2l6 2.5v5c0 4-3 7-6 8.5-3-1.5-6-4.5-6-8.5v-5z" fill="none" stroke="#fff" stroke-width="1.4"/><path d="M7 10l2 2 4-4" fill="none" stroke="#fff" stroke-width="1.4"/></svg></span>
        <p class="body"><b>Safety and Efficacy:</b> Reassure patients that the procedure is safe, with minimal risk, and has been shown to effectively support healing and tissue regeneration.</p>
      </div>
    </div>
    <div class="why-box">
      <h2 class="section__label">SECTION 5:</h2>
      <p class="section__sub" style="font-size:14px">Why Choose Our Clinic?</p>
      <div class="icon-row">
        <span class="icon-ring"><svg viewBox="0 0 20 20" aria-hidden="true"><g fill="none" stroke="#fff" stroke-width="1.4"><circle cx="10" cy="7" r="3.5"/><path d="M3 18c0-4 3-6 7-6s7 2 7 6"/></g></svg></span>
        <p class="body"><b>Expert Care:</b> Emphasize the expertise of your medical team in administering this advanced treatment.</p>
      </div>
      <div class="icon-row">
        <span class="icon-ring"><svg viewBox="0 0 20 20" aria-hidden="true"><path d="M3 4h14v9H9l-4 3v-3H3z" fill="none" stroke="#fff" stroke-width="1.4"/><path d="M7 8h6" stroke="#fff" stroke-width="1.4"/></svg></span>
        <p class="body"><b>Patient Testimonials:</b> Include a brief testimonial or quote from a satisfied patient (if available).</p>
      </div>
      <div class="icon-row">
        <span class="icon-ring"><svg viewBox="0 0 20 20" aria-hidden="true"><path d="M5 4l2.5 3-1.3 2a8 8 0 0 0 4 4l2-1.3 3 2.5-1.2 2.3C8.5 16.8 3 11.5 2.7 5.2z" fill="none" stroke="#fff" stroke-width="1.4"/></svg></span>
        <p class="body"><b>Contact Information:</b> Provide your clinic's contact details and encourage patients to schedule a consultation.</p>
      </div>
    </div>
  </div>

  <div class="panel panel--white">
    <p class="lead">Umbilical cord tissue allografts are increasingly being recognized for their potential in treating joint, soft tissue, and tendon injuries. The structural components of umbilical cord tissue offer several key benefits that make them particularly suitable for these applications:</p>
    <div class="benefits" style="top:136px">
      <div class="benefit">
        <span class="benefit__num">1</span>
        <h3 class="benefit__title">Collagen-Rich Matrix</h3>
        <p class="body"><b>Benefit:</b> The umbilical cord tissue is rich in collagen, which is essential for providing structural support to damaged tissues. This matrix serves as a scaffold that helps in the repair and regeneration of injured tissues by promoting the growth of new cells &amp; tissues in the affected area.</p>
        <p class="body"><b>Application:</b> Useful in joint, tendon, and soft tissue injuries where the repair of structural integrity is crucial for recovery.</p>
      </div>
      <div class="benefit">
        <span class="benefit__num">2</span>
        <h3 class="benefit__title">Anti-Inflammatory Properties</h3>
        <p class="body"><b>Benefit:</b> The tissue contains natural anti-inflammatory properties, which can help reduce inflammation at the injury site. By modulating the body's inflammatory response, umbilical cord tissue can help reduce pain and swelling, leading to faster recovery.</p>
        <p class="body"><b>Application:</b> Particularly beneficial in soft tissue &amp; tendon injuries where inflammation is a common symptom.</p>
      </div>
      <div class="benefit">
        <span class="benefit__num">3</span>
        <h3 class="benefit__title">Hyaluronic Acid Content</h3>
        <p class="body"><b>Benefit:</b> Hyaluronic acid is a component found in umbilical cord tissue that contributes to lubrication &amp; hydration. This helps in maintaining the elasticity and flexibility of the tissues, which is important for joint function and mobility.</p>
        <p class="body"><b>Application:</b> Ideal for joint injuries where maintaining smooth and frictionless movement is important.</p>
      </div>
      <div class="benefit">
        <span class="benefit__num">4</span>
        <h3 class="benefit__title">Growth Factors</h3>
        <p class="body"><b>Benefit:</b> Umbilical cord tissue is rich in growth factors that stimulate the body's natural healing processes. These factors promote cell proliferation, differentiation, and tissue repair, accelerating the healing of injured tissues.</p>
        <p class="body"><b>Application:</b> Effective in tendon and soft tissue injuries where enhanced healing is required to restore function.</p>
      </div>
    </div>
  </div>
</section>

</body>
</html>
```